Prairie Reading Alliance - Minds Unbound Website

We need a website designed for a PR + Marketing Campaign (Minds Unbound: Our Daily Craft) for the Prairie Reading Alliance (PRA), the largest statewide library association in the country.

The final design should communicate an empowerment to libraries, its innovative practices, and how they are helping and improving the lives of all communities (of all ages, backgrounds, experiences).

The look should be bold, captivating; meanwhile also simple, clean, easy-to-navigate.

LAYOUT (five pages total):
Page 1: Home – Intro
Animated logo transitioning into simple landing page.
Must feature #shelvesinmotion and eventually featuring video.

Page 2: About the Campaign
Graphics/photos optional, text below:
Broad Objectives and Goals
Minds Unbound: Our Daily Craft seeks to broaden the awareness of library services to the public and provide resources to librarians working in the state in order to promote libraries as vital, technology-centered institutions in the community.
The campaign provides a platform for the sharing of ideas and resources that strengthen the image of the library profession and the services provided by libraries in Texas.
Related goals include: providing librarians with the tools necessary to influence key supporters, shifting the perspectives of libraries as a center for books to a center for emerging technology and the cultivation of ideas, and spreading the message of the campaign through both traditional and social media outlets.
Librarians and information professionals are encouraged to actively participate in the campaign through social media outlets, using the hashtag #shelvesinmotion, and by contributing content in the Ideas Shared portion of the campaign website.

Page 3: Toolkit – downloadable items
Downloadable Campaign Materials for library professionals
Buttons leading to subpages or one large page covering the topics below

Page 4: Ideas Shared: What We Do: Interactive element page
Toolkit
Here are the tools and downloadable materials for #shelvesinmotion everywhere. Use these campaign designs to showcase the innovation happening in your library! Check back as we continue to update this page with new content.
Logos
Campaign logos in various formats for use on your own customized designs.
Print Materials
Flyers, bookmarks, posters and more!
Web & Interactive
Graphics for social media and the Web.
Coming soon: #shelvesinmotion campaign video!
PR & Marketing
Sample press releases, emails, and customizable content for a variety of library types: school, academic, public, and special.

Page 5: Contact Us Page
Can either be a sub-section of the About Us page, or a stand-alone link.
Standard submission form with the ability to upload documents for the Ideas Shared section.
Contact Us
Have a question or comment? Want to contribute a summary and photos or video of your innovative programs for the Ideas Shared section? Please get in touch!
NAME:
EMAIL:
PHONE:
ADDRESS: ?
MESSAGE:
ATTACHMENTS (upload)

MUST HAVE:
-Maintain the color-scheme of the logo (attached)
-The WEBSITE design must innovation and excitement. a contemporary design/layout that demonstrates vitality
-Somewhere on every page, we would like an interactive element for viewers, such as a stream from Chatterloop/Peepline with hashtags.
-Countdown to Campaign Launch
-Can we include animation? We are striving to create movement with the abstract icon in our log.

PLEASE AVOID:
-NO pastels, NO soft colors, nothing that might be considered feminine (pinks, etc); we do want to stear away from stereotypes (NO books, NO library buildings, NO reading conceptual designs) and standard icons (NO lightbulbs and NO lightning designs)

AUDIENCE/MARKET:
THE PUBLIC (also includes all kinds of librarians and their supporters: information, reference, school, public, special, law, academic, students, educators, administration, support staff, lay and advocates)

AUDIENCE/MARKET:

Requirements
Must have
• The final design should communicate an empowerment to libraries, its innovative practices, and how they are helping and improving the lives of all communities (of all ages, backgrounds, experiences).
• The look should be bold, captivating; meanwhile also simple, clean, easy-to-navigate.
• LAYOUT (five pages total):
• Page 1: Home – Intro
• Animated logo transitioning into simple landing page.
• Must feature #shelvesinmotion and eventually featuring video.
• Page 2: About the Campaign
• Graphics/photos optional, text below:
• Broad Objectives and Goals
• Minds Unbound: Our Daily Craft seeks to broaden the awareness of library services to the public and provide resources to librarians working in the state in order to promote libraries as vital, technology-centered institutions in the community.
• The campaign provides a platform for the sharing of ideas and resources that strengthen the image of the library profession and the services provided by libraries in Texas.
• Related goals include: providing librarians with the tools necessary to influence key supporters, shifting the perspectives of libraries as a center for books to a center for emerging technology and the cultivation of ideas, and spreading the message of the campaign through both traditional and social media outlets.
• Librarians and information professionals are encouraged to actively participate in the campaign through social media outlets, using the hashtag #shelvesinmotion, and by contributing content in the Ideas Shared portion of the campaign website.
• Page 3: Toolkit – downloadable items
• Downloadable Campaign Materials for library professionals
• Buttons leading to subpages or one large page covering the topics below
• Page 4: Ideas Shared: What We Do: Interactive element page
• Toolkit
• Here are the tools and downloadable materials for #shelvesinmotion everywhere. Use these campaign designs to showcase the innovation happening in your library! Check back as we continue to update this page with new content.
• Logos
• Campaign logos in various formats for use on your own customized designs.
• Print Materials
• Flyers, bookmarks, posters and more!
• Web & Interactive
• Graphics for social media and the Web.
• Coming soon: #shelvesinmotion campaign video!
• PR & Marketing
• Sample press releases, emails, and customizable content for a variety of library types: school, academic, public, and special.
• Page 5: Contact Us Page
• Can either be a sub-section of the About Us page, or a stand-alone link.
• Standard submission form with the ability to upload documents for the Ideas Shared section.
• Contact Us
• Have a question or comment? Want to contribute a summary and photos or video of your innovative programs for the Ideas Shared section? Please get in touch!
• NAME:
• EMAIL:
• PHONE:
• ADDRESS: ?
• MESSAGE:
• ATTACHMENTS (upload)
• MUST HAVE:
• -Maintain the color-scheme of the logo (attached)
• -The WEBSITE design must innovation and excitement. a contemporary design/layout that demonstrates vitality
• -Somewhere on every page, we would like an interactive element for viewers, such as a stream from Chatterloop/Peepline with hashtags.
• -Countdown to Campaign Launch
• -Can we include animation? We are striving to create movement with the abstract icon in our log.
Should not have
• PLEASE AVOID:
• -NO pastels, NO soft colors, nothing that might be considered feminine (pinks, etc); we do want to stear away from stereotypes (NO books, NO library buildings, NO reading conceptual designs) and standard icons (NO lightbulbs and NO lightning designs)

```html
<!DOCTYPE html>
<html lang="en">
<head>
<meta charset="utf-8">
<title>Minds Unbound – Prairie Reading Alliance</title>
<link rel="stylesheet" href="https://fonts.googleapis.com/css2?family=Marcellus&family=Open+Sans:ital,wght@0,400;0,600;1,400&display=swap">
<style>
:root{
  --brand:#2e9ad0;
  --brand-dark:#1f87bd;
  --ink:#2b2b2b;
  --body:#5a5a5a;
  --nav:#333;
  --footer:#2a2a2a;
  --white:#fff;
  --btn:#e6e6e6;
}
*{box-sizing:border-box;margin:0;padding:0}
html,body{width:1200px;height:1167px;overflow:hidden;background:var(--white)}
body{position:relative;font-family:"Open Sans",sans-serif;color:var(--body)}
.top-rule{position:absolute;left:0;top:0;width:1200px;height:4px;background:var(--brand)}
.site-header{position:absolute;left:0;top:4px;width:1200px;height:101px}
.brand{position:absolute;left:99px;top:28px;display:flex;align-items:center;gap:10px}
.brand-mark{width:30px;height:30px;border:2px solid var(--brand);border-radius:3px}
.brand-name{font-family:"Marcellus",serif;font-size:19px;color:var(--brand);line-height:1}
.brand-tag{font-family:"Marcellus",serif;font-size:9.5px;letter-spacing:3px;color:#9a9a9a;margin-top:4px}
.main-nav{position:absolute;top:42px;left:570px;display:flex;font-family:"Marcellus",serif;font-size:13px;color:var(--nav)}
.main-nav a{color:inherit;text-decoration:none;margin-right:23px}
.main-nav a.active{color:var(--brand)}
.search-icon{position:absolute;left:1086px;top:45px}
.hero{position:absolute;left:0;top:105px;width:1200px;height:405px;
  background:linear-gradient(120deg,#8a7a86 0%,#b9b3c4 30%,#6e6f95 55%,#5c4a6a 80%,#3d3048 100%)}
.hero-title{position:absolute;left:0;top:312px;width:1200px;text-align:center;font-family:"Marcellus",serif;font-size:40px;color:var(--white);letter-spacing:.5px}
.hero-arrow{position:absolute;top:295px}
.intro{position:absolute;left:98px;top:552px;width:530px}
.intro h2{font-family:"Marcellus",serif;font-weight:400;font-size:21px;color:var(--ink);margin-bottom:18px}
.intro p{font-size:12.5px;line-height:24px;margin-bottom:24px}
.read-more{font-size:12.5px;color:var(--brand);text-decoration:none;font-weight:600;position:relative;top:-10px}
.video-frame{position:absolute;left:657px;top:549px;width:445px;height:274px;border:1px solid #ddd;padding:4px}
.video-still{position:relative;width:100%;height:100%;background:linear-gradient(135deg,#e9f1f6 0%,#a9cde4 40%,#5f8fb0 75%,#c9a48c 100%)}
.video-play{position:absolute;left:193px;top:108px}
.video-side{position:absolute;right:10px;top:20px;display:flex;flex-direction:column;gap:5px}
.video-side span{width:31px;height:31px;background:#1c1c1c;border-radius:3px;display:flex;align-items:center;justify-content:center}
.video-bar{position:absolute;left:3px;bottom:5px;width:425px;height:31px;display:flex;gap:7px}
.bar-play{width:55px;height:31px;background:#1c1c1c;display:flex;align-items:center;justify-content:center}
.bar-track{flex:1;background:#1c1c1c;position:relative;display:flex;align-items:center;padding:0 8px;gap:8px;color:var(--white)}
.bar-time{position:absolute;left:-4px;top:-9px;background:var(--white);color:#111;font-size:9px;padding:0 3px;letter-spacing:.5px}
.bar-line{flex:1;height:9px;border:1px solid #555}
.bar-label{font-size:13px;font-weight:600}
.cta{position:absolute;left:0;top:868px;width:1200px;height:205px;background:var(--brand);text-align:center;color:var(--white)}
.cta h3{font-family:"Marcellus",serif;font-weight:400;font-size:22px;margin-top:33px}
.cta p{font-style:italic;font-size:14.5px;line-height:21px;width:620px;margin:12px auto 0}
.cta-button{display:inline-block;margin-top:18px;width:108px;height:41px;line-height:41px;background:var(--btn);color:#333;font-weight:600;font-size:14px;border-radius:2px;box-shadow:0 2px 0 #b9b9b9;text-decoration:none}
.site-footer{position:absolute;left:0;top:1073px;width:1200px;height:94px;background:var(--footer);color:#ddd}
.footer-brand{position:absolute;left:99px;top:30px;font-family:"Open Sans",sans-serif;font-weight:600;font-size:30px;color:#c8d6e0;letter-spacing:1px}
.footer-nav{position:absolute;left:0;width:1200px;top:24px;text-align:center;font-size:12.5px}
.footer-nav a{color:#ddd;text-decoration:none}
.footer-nav .sep{margin:0 7px}
.copyright{position:absolute;left:0;width:1200px;top:49px;text-align:center;font-size:12.5px}
.social{position:absolute;left:976px;top:28px;display:flex;gap:5px}
.social a{width:38px;height:38px;border:2px solid #eee;border-radius:50%;display:flex;align-items:center;justify-content:center;color:#eee;font-size:8px;text-decoration:none}
</style>
</head>
<body>
<div class="top-rule"></div>
<header class="site-header">
  <div class="brand">
    <span class="brand-mark"></span>
    <div>
      <div class="brand-name">Minds Unbound</div>
      <div class="brand-tag">OUR DAILY CRAFT</div>
    </div>
  </div>
  <nav class="main-nav">
    <a class="active" href="#">HOME</a>
    <a href="#">ABOUT THE CAMPAIGN</a>
    <a href="#">TOOLKIT</a>
    <a href="#">IDEAS SHARED</a>
    <a href="#">CONTACT US</a>
  </nav>
  <svg class="search-icon" width="15" height="15" viewBox="0 0 15 15" aria-label="Search"><circle cx="6" cy="6" r="4.5" fill="none" stroke="#2e9ad0" stroke-width="2"/><line x1="9.5" y1="9.5" x2="13.5" y2="13.5" stroke="#2e9ad0" stroke-width="2.4" stroke-linecap="round"/></svg>
</header>

<section class="hero" role="img" aria-label="Hands pointing at business charts on a tablet">
  <svg class="hero-arrow" style="left:39px" width="25" height="25" viewBox="0 0 25 25"><circle cx="12.5" cy="12.5" r="11" fill="none" stroke="#fff" stroke-width="1.5" opacity=".85"/><path d="M15 6.5 L8 12.5 L15 18.5 L13 12.5Z" fill="#fff" opacity=".85"/></svg>
  <svg class="hero-arrow" style="left:1134px" width="25" height="25" viewBox="0 0 25 25"><circle cx="12.5" cy="12.5" r="11" fill="none" stroke="#fff" stroke-width="1.5" opacity=".85"/><path d="M10 6.5 L17 12.5 L10 18.5 L12 12.5Z" fill="#fff" opacity=".85"/></svg>
  <h1 class="hero-title">MARKETING CAMPAIGN COMPANY</h1>
</section>

<section class="intro">
  <h2>#SHELVESINMOTION</h2>
  <p>2015-2016 Prairie Reading Alliance President Dana Whitlow charged the PRA PR &amp; Marketing Committee with the task of creating a big campaign to raise awareness about Texas libraries and the library profession in general, which would have wide appeal to all types of libraries and would be both an internal and external rebranding of today’s libraries.</p>
  <p>Together, the committee brainstormed and selected a campaign that would emphasize the innovation and technology-centered work being done in today’s libraries. Libraries are places where the creation and cultivation of ideas happen..</p>
  <a class="read-more" href="#">READ MORE &gt;&gt;</a>
</section>

<div class="video-frame">
  <div class="video-still" role="img" aria-label="Campaign video still: hands holding a tablet showing charts">
    <svg class="video-play" width="52" height="52" viewBox="0 0 52 52"><circle cx="26" cy="26" r="26" fill="#1c1c1c" opacity=".85"/><path d="M20 15 L37 26 L20 37Z" fill="#fff"/></svg>
    <div class="video-side">
      <span><svg width="17" height="15" viewBox="0 0 17 15"><path d="M8.5 14 L1.5 7 A3.8 3.8 0 0 1 8.5 2.5 A3.8 3.8 0 0 1 15.5 7Z" fill="#fff"/></svg></span>
      <span><svg width="16" height="16" viewBox="0 0 16 16"><path d="M15 1 L1 7 L6 9 L7 15 L10 10 Z" fill="#fff"/></svg></span>
    </div>
    <div class="video-bar">
      <div class="bar-play"><svg width="16" height="16" viewBox="0 0 16 16"><path d="M2 1 L15 8 L2 15Z" fill="#fff"/></svg></div>
      <div class="bar-track">
        <span class="bar-time">02:33</span>
        <span class="bar-line"></span>
        <span class="bar-label">HD</span>
        <span class="bar-label">Reelbox</span>
      </div>
    </div>
  </div>
</div>

<section class="cta">
  <h3>HAVE A QUESTION OR COMMENT?</h3>
  <p>Want to contribute a summary and photos or video of your innovative programs for the Ideas Shared section? Please get in touch!</p>
  <a class="cta-button" href="#">CONTACT US</a>
</section>

<footer class="site-footer">
  <div class="footer-brand">PRA</div>
  <nav class="footer-nav">
    <a href="#">Home</a><span class="sep">|</span><a href="#">About the Campaign</a><span class="sep">|</span><a href="#">Toolkit</a><span class="sep">|</span><a href="#">Ideas shared</a><span class="sep">|</span><a href="#">Contact us</a>
  </nav>
  <div class="copyright">Copyrights © Minds Unbound.All rights Reserved.</div>
  <div class="social">
    <a href="#">Chatter</a>
    <a href="#">Peep</a>
    <a href="#">Huddle</a>
  </div>
</footer>
</body>
</html>
```